website for 'thebrightnook' which is a specialise tutoring company for children with learning difficu

We need a website for a new business that is focused on assessment and then specialised tutoring for young children with learning difficulties. The website needs to be simple but fun and fresh. We have an existing logo (uploaded) that needs to be the building block for the website. The website doesn't need to be overly content-heavy.

Target Market(s)

parents

Industry/Entity Type

Education

Number of Pages Required

3 page

Font styles to use
Other font styles liked:
• possibly matched to the logo

Requirements
Must have
• a initial front page which introduces the business and provides contact details, a second page that will allow for a more content-heavy section, a third page which focuses on introducing the staff (initially 3 staff ),

```html
<!DOCTYPE html>
<html lang="en">
<head>
<meta charset="utf-8">
<title>thebrightnook – specialised learning for children</title>
<link href="https://fonts.googleapis.com/css2?family=Roboto+Slab:wght@300;400&family=Open+Sans:wght@400;600&display=swap" rel="stylesheet">
<style>
:root{
  --green:#8dc63f;
  --orange:#fbb316;
  --yellow:#fbbd2e;
  --ink:#4a4a4a;
  --muted:#8a8a8a;
  --line:#e3e3e3;
  --white:#ffffff;
}
*{margin:0;padding:0;box-sizing:border-box}
html,body{width:1200px;height:2830px;overflow:hidden;background:var(--white)}
body{position:relative;font-family:'Open Sans',sans-serif;color:var(--ink)}
.slab{font-family:'Roboto Slab',serif;font-weight:300}
.abs{position:absolute}
a{color:inherit;text-decoration:none}

/* header */
.brand{left:79px;top:95px;display:flex;align-items:center;gap:12px}
.brand-dot{width:30px;height:30px;border-radius:50%;background:var(--green)}
.brand-name{font-family:'Roboto Slab',serif;font-weight:400;font-size:44px;color:#5a5a5a;letter-spacing:-1px}
.brand-tag{left:79px;top:164px;font-family:'Roboto Slab',serif;font-size:13px;letter-spacing:2.4px;color:#777}
.nav{top:56px;font-size:14px;color:#444}
.nav.active::after{content:"";position:absolute;left:0;right:0;top:26px;height:3px;background:var(--green)}

/* hero */
.hero-title{left:108px;top:252px;font-size:52px;color:var(--green)}
.hero-sub{left:108px;top:320px;font-size:23px;color:#444}
.hero-text{left:108px;top:366px;width:470px;font-size:14px;line-height:26px;color:var(--muted)}
.btn-solid{left:108px;top:464px;width:170px;height:48px;background:var(--orange);color:var(--white);font-family:'Roboto Slab',serif;font-size:16px;display:flex;align-items:center;justify-content:center;border-radius:2px}
.hero-photo{left:689px;top:113px;width:443px;height:531px;background:radial-gradient(circle at 55% 55%,#f2d9c4 0,#e9eef4 45%,#ffffff 75%)}
.dots{left:574px;top:606px;display:flex;gap:5px}
.dots span{width:9px;height:9px;border-radius:50%;background:#cfe6ad}
.dots span:first-child{background:var(--green)}

/* welcome */
.welcome{left:0;top:644px;width:1200px;height:349px;background:var(--green);color:var(--white);text-align:center}
.welcome h2{position:absolute;top:60px;width:100%;font-size:38px;font-weight:300}
.welcome p{position:absolute;left:170px;top:122px;width:860px;font-size:12.5px;line-height:29px}
.btn-ghost{top:230px;width:174px;height:50px;border:1px solid rgba(255,255,255,.85);border-radius:2px;display:flex;align-items:center;justify-content:center;font-family:'Roboto Slab',serif;font-size:16px}

/* sections */
.sec-title{font-size:34px;color:#444}
.sec-sub{font-size:13px;color:#555}
.service-icon{width:88px;height:88px;border-radius:50%;background:var(--green);display:flex;align-items:center;justify-content:center}
.service-name{font-family:'Roboto Slab',serif;font-size:20px;color:#444}
.service-text{width:200px;font-size:13px;line-height:24px;color:var(--muted)}

.gallery{left:0;top:1459px;width:1200px;height:609px;background:var(--yellow)}
.gallery-title{left:98px;top:1516px;color:var(--white)}
.gallery-sub{left:98px;top:1566px;color:var(--white)}
.photo{width:238px}

.quote{width:270px;font-size:12.5px;line-height:24px;color:var(--muted)}
.quote-mark{font-family:'Roboto Slab',serif;font-size:34px;color:#bbb;line-height:1}
.avatar{width:56px;height:56px;border-radius:50%;border:3px solid var(--green);background:linear-gradient(#e4d7c8,#b7a48f)}
.client-name{font-family:'Roboto Slab',serif;font-size:12px;color:var(--green);letter-spacing:.5px}
.client-role{font-size:11px;color:#666}

.rule{left:0;width:1200px;height:1px;background:var(--line)}
.foot-h{top:2515px;font-family:'Roboto Slab',serif;font-size:20px;color:#444}
.foot-list{top:2554px;font-size:12px;line-height:27.5px;color:#666;list-style:none}
.email-field{left:98px;top:2581px;width:334px;height:36px;border:1px solid #ccc;font-size:12px;color:#888;padding:0 14px;display:flex;align-items:center}
.btn-subscribe{left:98px;top:2632px;width:128px;height:35px;background:var(--green);color:var(--white);font-size:14px;font-weight:600;display:flex;align-items:center;justify-content:center}
.social{top:2678px;display:flex;gap:8px;left:921px}
.social span{width:34px;height:34px;border-radius:50%}
.copyright{top:2776px;left:0;width:1200px;text-align:center;font-size:12px;color:#666}
</style>
</head>
<body>

<header>
  <div class="abs brand"><span class="brand-dot"></span><span class="brand-name">thebrightnook</span></div>
  <div class="abs brand-tag">specialised learning for children</div>
  <nav>
    <a class="abs nav active" style="left:553px">Home</a>
    <a class="abs nav" style="left:659px">About us</a>
    <a class="abs nav" style="left:783px">Services</a>
    <a class="abs nav" style="left:905px">Testimonials</a>
    <a class="abs nav" style="left:1110px">Contact us</a>
  </nav>
</header>

<section class="hero">
  <h1 class="abs slab hero-title">We give training</h1>
  <p class="abs hero-sub">to kids with learning difficulties.</p>
  <p class="abs hero-text">Lorem Ipsum is simply dummy text of the printing and typesetting industry. Lorem Ipsum has been the industry's standard dummy text ever since the 1500s</p>
  <a class="abs btn-solid">Contact Here!</a>
  <div class="abs hero-photo" role="img" aria-label="Photo of a curious young child scratching her head under pink and purple speech bubbles with exclamation and question marks"></div>
  <div class="abs dots"><span></span><span></span><span></span><span></span></div>
</section>

<section class="abs welcome">
  <h2 class="slab">Welcome to Bright Nook</h2>
  <p>Lorem Ipsum is simply dummy text of the printing and typesetting industry. Lorem Ipsum has been the industry's standard dummy text ever since the 1500s, when an unknown printer took a galley of type and scrambled it to make a type specimen book. It has survived not only five centuries, but also the leap into electronic typesetting, remaining essentially unchanged.</p>
  <a class="abs btn-ghost" style="left:413px">Read more info</a>
  <a class="abs btn-ghost" style="left:611px">Contact Here!</a>
</section>

<section class="services">
  <h2 class="abs slab sec-title" style="left:98px;top:1052px">Our Services</h2>
  <p class="abs sec-sub" style="left:98px;top:1100px">Lorem Ipsum is simply dummy text of the printing and typesetting industry. Lorem Ipsum has been the industry's standard dummy</p>

  <div class="abs service-icon" style="left:98px;top:1169px"><svg width="44" height="44" viewBox="0 0 44 44" fill="none" stroke="#fff" stroke-width="2"><rect x="8" y="9" width="28" height="19"/><path d="M22 28v8M16 38l6-6 6 6M22 5v4"/></svg></div>
  <div class="abs service-icon" style="left:371px;top:1169px"><svg width="44" height="44" viewBox="0 0 44 44" fill="none" stroke="#fff" stroke-width="2"><circle cx="22" cy="18" r="9"/><path d="M9 38c2-8 8-11 13-11s11 3 13 11"/></svg></div>
  <div class="abs service-icon" style="left:641px;top:1169px"><svg width="44" height="44" viewBox="0 0 44 44" fill="none" stroke="#fff" stroke-width="2"><ellipse cx="17" cy="15" rx="7" ry="9"/><ellipse cx="28" cy="19" rx="7" ry="9"/><path d="M17 24l2 14M28 28l-5 10"/></svg></div>
  <div class="abs service-icon" style="left:913px;top:1169px"><svg width="44" height="44" viewBox="0 0 44 44" fill="none" stroke="#fff" stroke-width="2"><path d="M14 7h16v9a8 8 0 0 1-16 0zM14 10H8c0 6 3 9 6 9M30 10h6c0 6-3 9-6 9M22 24v8M15 37h14v-5H15z"/></svg></div>

  <h3 class="abs service-name" style="left:103px;top:1276px">Training</h3>
  <h3 class="abs service-name" style="left:372px;top:1276px">Activities</h3>
  <h3 class="abs service-name" style="left:644px;top:1276px">Events</h3>
  <h3 class="abs service-name" style="left:914px;top:1276px">Compatitions</h3>
  <p class="abs service-text" style="left:103px;top:1310px">Lorem Ipsum is simply dummy text of the printing and typesetting industry...</p>
  <p class="abs service-text" style="left:373px;top:1310px">Lorem Ipsum is simply dummy text of the printing and typesetting industry...</p>
  <p class="abs service-text" style="left:644px;top:1310px">Lorem Ipsum is simply dummy text of the printing and typesetting industry...</p>
  <p class="abs service-text" style="left:916px;top:1310px">Lorem Ipsum is simply dummy text of the printing and typesetting industry...</p>
</section>

<section>
  <div class="abs gallery"></div>
  <h2 class="abs slab sec-title gallery-title">Photo Gallery</h2>
  <p class="abs sec-sub gallery-sub">Lorem Ipsum is simply dummy text of the printing and typesetting industry. Lorem Ipsum has been the industry's standard dummy</p>
  <div class="abs photo" style="left:98px;top:1623px;height:175px;background:linear-gradient(135deg,#e8d6d0,#c9a8b8)" role="img" aria-label="Toddlers playing with colourful blocks and toys"></div>
  <div class="abs photo" style="left:353px;top:1623px;height:175px;background:linear-gradient(#4a7fc4,#8fb870)" role="img" aria-label="Two boys in football kit on a grass field"></div>
  <div class="abs photo" style="left:608px;top:1623px;height:175px;background:linear-gradient(135deg,#c48a6a,#7c9a74)" role="img" aria-label="Teacher drawing with children at a classroom table"></div>
  <div class="abs photo" style="left:864px;top:1623px;height:175px;background:linear-gradient(135deg,#b89a84,#e6e0d8)" role="img" aria-label="Group of smiling children giving thumbs up"></div>
  <div class="abs photo" style="left:98px;top:1817px;height:178px;background:linear-gradient(#9fb0c4,#b48a5a)" role="img" aria-label="Children dressed as superheroes with capes outdoors"></div>
  <div class="abs photo" style="left:353px;top:1817px;height:178px;background:linear-gradient(#7fae4a,#c8d88a)" role="img" aria-label="Child running through a green meadow"></div>
  <div class="abs photo" style="left:608px;top:1817px;height:178px;background:linear-gradient(#3aa7d8,#1e7fbf)" role="img" aria-label="Three children with swimming goggles in a pool"></div>
  <div class="abs photo" style="left:864px;top:1817px;height:178px;background:linear-gradient(135deg,#e8e8e8,#9eb8c8)" role="img" aria-label="Children working at computer keyboards"></div>
</section>

<section class="testimonials">
  <h2 class="abs slab sec-title" style="left:0;width:1200px;text-align:center;top:2124px">Happy Client's</h2>
  <p class="abs sec-sub" style="left:0;width:1200px;text-align:center;top:2182px">Lorem Ipsum is simply dummy text of the printing and typesetting industry. Lorem Ipsum has been the industry's standard dummy</p>

  <span class="abs quote-mark" style="left:102px;top:2240px">“</span>
  <span class="abs quote-mark" style="left:371px;top:2318px">”</span>
  <p class="abs quote" style="left:128px;top:2248px">Lorem Ipsum is simply dummy text of the printing and typesetting industry. Lorem Ipsum has been the industry's standard dummy text ever since...</p>
  <span class="abs quote-mark" style="left:458px;top:2240px">“</span>
  <span class="abs quote-mark" style="left:727px;top:2318px">”</span>
  <p class="abs quote" style="left:484px;top:2248px">Lorem Ipsum is simply dummy text of the printing and typesetting industry. Lorem Ipsum has been the industry's standard dummy text ever since...</p>
  <span class="abs quote-mark" style="left:813px;top:2240px">“</span>
  <span class="abs quote-mark" style="left:1083px;top:2318px">”</span>
  <p class="abs quote" style="left:840px;top:2248px">Lorem Ipsum is simply dummy text of the printing and typesetting industry. Lorem Ipsum has been the industry's standard dummy text ever since...</p>

  <div class="abs avatar" style="left:99px;top:2357px" role="img" aria-label="Client portrait"></div>
  <div class="abs avatar" style="left:454px;top:2357px" role="img" aria-label="Client portrait"></div>
  <div class="abs avatar" style="left:810px;top:2357px" role="img" aria-label="Client portrait"></div>
  <p class="abs client-name" style="left:165px;top:2367px">MARLON REEDY</p>
  <p class="abs client-name" style="left:520px;top:2367px">MARLON REEDY</p>
  <p class="abs client-name" style="left:876px;top:2367px">MARLON REEDY</p>
  <p class="abs client-role" style="left:165px;top:2389px">Business man</p>
  <p class="abs client-role" style="left:520px;top:2389px">Business man</p>
  <p class="abs client-role" style="left:876px;top:2389px">Business man</p>
</section>

<footer>
  <div class="abs rule" style="top:2478px"></div>
  <h4 class="abs foot-h" style="left:98px">Newsletter signup</h4>
  <p class="abs" style="left:98px;top:2556px;font-size:12px;color:#666">Get our recent updates through your email id</p>
  <div class="abs email-field">Enter your email id</div>
  <a class="abs btn-subscribe">Subscribe</a>

  <h4 class="abs foot-h" style="left:510px">Welcome</h4>
  <ul class="abs foot-list" style="left:510px"><li>Home</li><li>About us</li><li>Services</li><li>Photogallery</li><li>Testimonials</li><li>Contact us</li></ul>

  <h4 class="abs foot-h" style="left:706px">Information</h4>
  <ul class="abs foot-list" style="left:706px"><li>Terms &amp; Conditions</li><li>Privacy Policy</li><li>Disclaimer</li><li>Sitemap</li></ul>

  <h4 class="abs foot-h" style="left:921px">Contact info</h4>
  <ul class="abs foot-list" style="left:921px;line-height:31px">
    <li>120 STreet name, City name.</li>
    <li>Country name : 6410552</li>
    <li><svg width="12" height="12" viewBox="0 0 12 12" style="vertical-align:-1px"><path d="M2 1l2.5 0 1 3-1.5 1a7 7 0 0 0 3 3l1-1.5 3 1V10a1 1 0 0 1-1 1A10 10 0 0 1 1 2a1 1 0 0 1 1-1z" fill="#8dc63f"/></svg> ( 6410 ) 552 781</li>
    <li><svg width="13" height="10" viewBox="0 0 13 10" style="vertical-align:0"><rect width="13" height="10" fill="#8dc63f"/><path d="M0 0l6.5 5L13 0" stroke="#fff" fill="none"/></svg> info@brightnook.com</li>
  </ul>
  <div class="abs social">
    <span style="background:#3b5b99"></span>
    <span style="background:#1f7bb6"></span>
    <span style="background:#f0a21e"></span>
    <span style="background:#3fa9e0"></span>
  </div>

  <div class="abs rule" style="top:2751px"></div>
  <p class="abs copyright">Copyright © 2016, Bright Nook. All rights reserved.</p>
</footer>

</body>
</html>
```